Weight Loss Challenge Social Media Graphics

Create 6-7 individual social media graphics (square size) to encourage folks to join our weight loss challenge. For the color scheme of the graphics, use the color palette attached

Note: each graphic can contain any of the stock photography attached or just the single picture of me (brown shirt) but a few should be ONLY the text
For some graphics we can say: JOIN US!
For some graphics, use only TEXT based

Target Market(s)

primarily women who want to get healthy

Industry/Entity Type

health and weight loss

Requirements
Must have
• The largest text should be: Ninety Days Bold

```html
<!DOCTYPE html>
<html lang="en">
<head>
<meta charset="utf-8">
<title>Ninety Days Bold – Challenge Announcement</title>
<link rel="stylesheet" href="https://fonts.googleapis.com/css2?family=Josefin+Sans:wght@200&family=Raleway:wght@400&family=Cormorant+Garamond:wght@500&display=swap">
<style>
  :root {
    --rose: #c3a096;
    --cream: #f4dfd2;
    --text-cream: #f6e6da;
    --tan: #b98a60;
    --brown: #7a4a33;
    --black: #1c1a1c;
  }
  html, body {
    margin: 0;
    padding: 0;
    width: 1200px;
    height: 1200px;
    overflow: hidden;
    background: var(--rose);
  }
  .poster {
    position: relative;
    width: 1200px;
    height: 1200px;
    overflow: hidden;
    background: var(--rose);
  }
  .backdrop {
    position: absolute;
    inset: 0;
  }
  .headline {
    position: absolute;
    left: 40px;
    top: 213px;
    margin: 0;
    font-family: "Josefin Sans", sans-serif;
    font-weight: 200;
    font-size: 128px;
    line-height: 180px;
    color: var(--text-cream);
    white-space: nowrap;
    z-index: 2;
  }
  .offer {
    position: absolute;
    left: 0;
    width: 640px;
    top: 680px;
    margin: 0;
    text-align: center;
    font-family: "Raleway", sans-serif;
    font-weight: 400;
    font-size: 40px;
    line-height: 67px;
    letter-spacing: 0.5px;
    color: var(--text-cream);
  }
  .start-date {
    position: absolute;
    left: 48px;
    top: 976px;
    margin: 0;
    font-family: "Cormorant Garamond", serif;
    font-weight: 500;
    font-size: 40px;
    letter-spacing: 2.5px;
    color: var(--text-cream);
    white-space: nowrap;
  }
  .host-photo {
    position: absolute;
    left: 720px;
    top: 168px;
    width: 470px;
    height: 1032px;
    border-radius: 24px 24px 0 0;
    background: linear-gradient(180deg, var(--brown) 0%, var(--tan) 30%, var(--tan) 62%, var(--black) 70%, var(--black) 100%);
  }
</style>
</head>
<body>
<main class="poster">
  <svg class="backdrop" width="1200" height="1200" viewBox="0 0 1200 1200" aria-hidden="true">
    <rect width="1200" height="1200" fill="var(--rose)"/>
    <circle cx="-18" cy="-222" r="413" fill="var(--cream)"/>
    <ellipse cx="1320" cy="1080" rx="360" ry="636" fill="var(--cream)"/>
  </svg>

  <div class="host-photo" role="img" aria-label="Photo of the smiling challenge host in a camel turtleneck and black high-waisted jeans, hand on hip"></div>

  <h1 class="headline">Ninety Days<br>Bold</h1>

  <p class="offer">LOSE UP TO 20 POUNDS<br>IN 6 WEEKS!</p>

  <p class="start-date">BEGINS MONDAY, JAN 6TH</p>
</main>
</body>
</html>
```